Client Publishing Agency Brochure

We need a company brochure for a new company based in Cape Town, South Africa called Velvet Harbour Studios (VHS).

We need a brochure marketing our publishing agency (vhs:inkwell) and our creative, interactive & print production division (vhs:forge). Develop a fresh design concept which will direct the design of our new website in the near future. (So don't pay attention to our current web page. It does not reflect our brand).

vhs:inkwell is a content marketing agency offering our clients (B2B, B2C, NPO, Professional & Membership Organizations) branded publishing to build trust, authority and relationships with their customers. A typical content strategy may include communication through client print or online magazine, newsletters, microsite, website, social technology and plenty more). We want to communicate that company's need to change their mind set from promoting their products and begin to invest in developing a relationship with their potential & existing customers. The drive is a Return On Objectives (business & marketing objectives) and interest is a Return On Investment (ROI).

vhs:forge is a creative, interactive & print production agency which supports our client's marketing collateral needs.
Updates

Hi Designers,

This is a response to questions posted earlier to assist you in your project.

Q.What will the size of brochure be?
A. A4 size with folder flap for the back cover

Q.Will it be a three panels double sided?
A. Depends on your creative concept. But if you make a 3 panel dbl side then layout two version for print (double sided 3 panel) and digital pdf (single pdf pages in sequence).

Q.The images that you supplied I know are just samples, What type of images are 
required? 
A. Depends on your creative concept. Let the style of the logo inspire you. What I liked in the examples is the classic, premium, quality feel. So no business stock imagery. I'm also a creative agency so that message needs to come through. Illustrated styles are welcome.

Q.Should design have same feel as your website? 
A. No. Our website is pending the outcome of the brochure. The brochure will be our creative direction for our new website. So creative an inspiring and clean brochure.

Please feel free to post additional questions. Good Luck and thank you for your participation.

Project Deadline Extended
Reason: The designers have not produced a style and concept that reflects our brand. Would like to guide them more to reach the right look for our company.

Hi Designers...

I have not been happy with the quality of ideas and execution of those ideas. This I understand could a combination of a poor brief and a non-guarenteed project.

I have rectified the brief and have guaranteed the award. Please don't hold back on your creativity and return the guarantee for high quality.

Please ask me any questions to better understand what we are looking for.

Remember. This brochure is a new design concept. Do not visit the web page for inspiration. The new design concept for the brochure will set the tone and inspire a new website.

Lets create a beautiful product together.

Thank you for your participation.

Project Deadline Extended
Reason: Designers are not following the brief, and not respecting the logo and colour policies/guidelines and those who are submitting work are not asking questions throughout the process to get a better understanding of what we need. All design submissions are always at the last minute. And some designers are are not real designers and using web development software to produce print designs. More importantly after taking time to advise designers of changes, no effort is made by designers to make changes. Each designer submits 1 idea and think that they are going to win the lottery. Where is the work ethic and quality of service? Where are the submissions from the designers who accepted the participation fee? There were a few designers who promised participation and never showed up. Maybe it all our fault? But we not happy with the service and level of creativity. Not sure if these designers are taking pride in their work or not. I know a few of you are.

Target Market(s)

B2B, B2C, NPO, Professional & Membership Organizations - Make up professionals and decision makers across sectors from Shipping and Logistics, Manufacturing, Legal to Art & Culture.

Industry/Entity Type

Communication

Requirements
Must have
• Size: A4
x 2 Panels
+ Folder flap (for A4 Paper, business card slot)
Styled map to our premises. See map attachment for example.

Pages: 10 including cover (if you need more than this let your design motivate the need for more pages)

(See logo use eps file)
(See colour use eps file)

Nice to have
• Styled map to our premises. See attachment for example.
Should not have
• Do not take any inspiration from our website. It is just a free template to show customers that it is still under construction.

Do not include stock symbols and typical business stock images. Remember we are a creative offering, so our brochure should show originality, innovation and individuality.

```html
<!DOCTYPE html>
<html lang="en">
<head>
<meta charset="utf-8">
<title>Velvet Harbour Studios — Brochure Cover Spread</title>
<link rel="stylesheet" href="https://fonts.googleapis.com/css2?family=Poppins:wght@300;700&display=swap">
<style>
  :root {
    --ink: #000000;
    --paper: #ffffff;
    --glow-mid: #b9b9b9;
    --glow-edge: #5a5a5a;
    --fold-line: #8a8a8a;
    --ring-line: rgba(255, 255, 255, 0.75);
  }
  * { margin: 0; padding: 0; box-sizing: border-box; }
  html, body {
    width: 1200px;
    height: 848px;
    overflow: hidden;
    background: var(--ink);
  }
  .spread {
    position: relative;
    width: 1200px;
    height: 848px;
    background: var(--ink);
    font-family: "Poppins", "Century Gothic", sans-serif;
  }
  .panel-back {
    position: absolute;
    left: 0; top: 0;
    width: 597px; height: 848px;
    background: var(--ink);
  }
  .panel-cover {
    position: absolute;
    left: 597px; top: 0;
    width: 603px; height: 848px;
    overflow: hidden;
    background:
      radial-gradient(circle at 293px 420px,
        var(--paper) 0px,
        var(--paper) 150px,
        #ededed 200px,
        var(--glow-mid) 260px,
        var(--glow-edge) 320px,
        #1a1a1a 390px,
        var(--ink) 430px);
  }
  .cover-ring {
    position: absolute;
    left: 0; top: 0;
    width: 603px; height: 848px;
  }
  .fold-mark {
    position: absolute;
    bottom: 0;
    width: 1px;
    height: 40px;
    background: var(--fold-line);
  }
  .fold-mark--spine { left: 597px; }
  .fold-mark--edge { left: 3px; }
  .brand-name {
    position: absolute;
    left: 0; top: 320px;
    width: 603px;
    text-align: center;
    padding-left: 10px;
    font-weight: 700;
    font-size: 150px;
    line-height: 180px;
    letter-spacing: 6px;
    color: var(--ink);
  }
  .brand-tagline {
    position: absolute;
    left: 0; top: 503px;
    width: 603px;
    text-align: center;
    padding-left: 14px;
    font-weight: 300;
    font-size: 12.5px;
    letter-spacing: 0.6px;
    word-spacing: 2px;
    color: var(--ink);
  }
</style>
</head>
<body>
  <main class="spread">
    <section class="panel-back" aria-label="Back cover"></section>

    <section class="panel-cover" aria-label="Front cover">
      <svg class="cover-ring" viewBox="0 0 603 848" aria-hidden="true">
        <circle cx="293" cy="420" r="205" fill="none" stroke="var(--ring-line)" stroke-width="1"/>
      </svg>
      <h1 class="brand-name">vhs</h1>
      <p class="brand-tagline">velvet harbour studios : custom &nbsp;creative &nbsp;intelligent</p>
    </section>

    <span class="fold-mark fold-mark--edge"></span>
    <span class="fold-mark fold-mark--spine"></span>
  </main>
</body>
</html>
```